Financial Services Business Card Design

We are a financial services company Based in London, offering Short term Funding Solutions for companies, raising anywhere between £20,000 and £25million pounds.

The Card must have a professional look as it is going to be handed out to professionals I.E Solicitors, Accountants, Company directors and Business owners.

See Attached our company Logo

Industry/Entity Type

Business

Contact Information for Business Card

Lewis Thorncroft
Suite 41
R K House
Bramblecote Lane
Kestrelford
HP19 4QX

```html
<!DOCTYPE html>
<html lang="en">
<head>
<meta charset="utf-8">
<title>Harrowgate Capital – Business Card</title>
<link href="https://fonts.googleapis.com/css2?family=Arimo:wght@400;700&display=swap" rel="stylesheet">
<style>
  :root {
    --brand-blue: #1f6fbf;
    --brand-blue-dark: #185fa8;
    --brand-green: #3aa64a;
    --text-grey: #5a5a5a;
    --card-white: #fbfbfb;
    --backdrop: #ecebe8;
  }
  * { margin: 0; padding: 0; box-sizing: border-box; }
  html, body { width: 1200px; height: 1023px; overflow: hidden; }
  body {
    background: var(--backdrop);
    font-family: "Arimo", Arial, sans-serif;
    position: relative;
  }
  .card {
    position: absolute;
    width: 640px;
    height: 366px;
    border-radius: 4px;
    box-shadow: 0 10px 28px rgba(0,0,0,0.22);
    overflow: hidden;
  }

  /* Front */
  .card-front { left: 70px; top: 80px; background: var(--card-white); }
  .brand {
    position: absolute; left: 44px; top: 48px;
    display: flex; align-items: center; gap: 12px;
  }
  .brand-dot {
    width: 26px; height: 26px; border-radius: 50%;
    background: var(--brand-blue);
    flex: none;
  }
  .brand-name {
    color: var(--brand-blue); font-weight: 700; font-size: 32px;
    letter-spacing: 0.5px; white-space: nowrap;
  }
  .person { position: absolute; left: 44px; top: 128px; }
  .person-name { color: var(--brand-blue); font-weight: 700; font-size: 23px; }
  .person-title { color: var(--brand-green); font-size: 17px; margin-top: 4px; }
  .contacts {
    position: absolute; left: 44px; top: 214px;
    list-style: none; color: var(--text-grey); font-size: 15px;
  }
  .contacts li { display: flex; align-items: center; gap: 10px; height: 24px; white-space: nowrap; }
  .contacts svg { width: 14px; height: 14px; fill: var(--brand-blue); flex: none; }
  .contacts .web-accent { color: var(--brand-blue); }
  .address {
    position: absolute; left: 390px; top: 214px;
    font-style: normal; color: var(--text-grey); font-size: 15px; line-height: 24px;
    white-space: nowrap;
  }
  .front-band {
    position: absolute; left: 0; right: 0; bottom: 0; height: 26px;
    background: var(--brand-blue);
    border-top: 4px solid var(--brand-green);
  }

  /* Back */
  .card-back {
    left: 490px; top: 570px;
    background: radial-gradient(ellipse at 45% 40%, #2a7fd0 0%, var(--brand-blue) 55%, var(--brand-blue-dark) 100%);
  }
  .back-brand {
    position: absolute; left: 0; right: 0; top: 130px;
    display: flex; justify-content: center; align-items: center; gap: 14px;
  }
  .back-brand .brand-dot { background: #ffffff; width: 30px; height: 30px; }
  .back-brand .brand-name { color: #ffffff; font-size: 38px; }
  .back-footer {
    position: absolute; left: 40px; right: 40px; bottom: 48px;
    display: flex; align-items: center; gap: 16px;
    color: #ffffff; font-size: 14px; letter-spacing: 0.5px; white-space: nowrap;
  }
  .back-footer .rule { flex: 1; height: 1px; background: rgba(255,255,255,0.7); }
</style>
</head>
<body>

<section class="card card-front" aria-label="Business card front">
  <div class="brand">
    <span class="brand-dot"></span>
    <span class="brand-name">Harrowgate Capital</span>
  </div>

  <div class="person">
    <div class="person-name">Lewis Thorncroft</div>
    <div class="person-title">Managing Director</div>
  </div>

  <ul class="contacts">
    <li>
      <svg viewBox="0 0 24 24" aria-hidden="true"><path d="M6.6 10.8a15 15 0 0 0 6.6 6.6l2.2-2.2c.3-.3.7-.4 1-.2 1.1.4 2.3.6 3.6.6.6 0 1 .4 1 1V20c0 .6-.4 1-1 1C10.6 21 3 13.4 3 4c0-.6.4-1 1-1h3.5c.6 0 1 .4 1 1 0 1.3.2 2.5.6 3.6.1.3 0 .7-.2 1z"/></svg>
      +987 41 62 30
    </li>
    <li>
      <svg viewBox="0 0 24 24" aria-hidden="true"><path d="M2 5h20v14H2z M2 5l10 8 10-8" fill="none" stroke="#1f6fbf" stroke-width="2.4"/></svg>
      info@harrowgatecapital.com
    </li>
    <li>
      <svg viewBox="0 0 24 24" aria-hidden="true"><g fill="none" stroke="#1f6fbf" stroke-width="2"><circle cx="12" cy="12" r="9.5"/><ellipse cx="12" cy="12" rx="4.2" ry="9.5"/><path d="M2.5 12h19M4 7h16M4 17h16"/></g></svg>
      <span>www.<span class="web-accent">harrowgatecapital</span>.com</span>
    </li>
  </ul>

  <address class="address">
    Suite 41 R K House<br>
    Bramblecote Lane Kestrelford<br>
    HP19 4QX
  </address>

  <div class="front-band"></div>
</section>

<section class="card card-back" aria-label="Business card back">
  <div class="back-brand">
    <span class="brand-dot"></span>
    <span class="brand-name">Harrowgate Capital</span>
  </div>
  <div class="back-footer">
    <span class="rule"></span>
    <span>www.harrowgatecapital.com</span>
    <span class="rule"></span>
  </div>
</section>

</body>
</html>
```